Boarder on lantern and hill label

Hi - happy to pay for the boarder version but would like to see it so I can approve. Please add thin red boarder on sides and bottom on the label I selected as the winner.

```html
<!DOCTYPE html>
<html lang="en">
<head>
<meta charset="utf-8">
<title>Lantern and Hill – Fresh Mushrooms Label</title>
<link rel="stylesheet" href="https://fonts.googleapis.com/css2?family=Anton&family=Oswald:wght@600&family=Encode+Sans+Condensed:wght@400;700&display=swap">
<style>
  :root {
    --label-red: #bd1e2d;
    --label-white: #ffffff;
    --fresh-yellow: #fdc65f;
    --ink-black: #000000;
  }
  * { margin: 0; padding: 0; box-sizing: border-box; }
  html, body {
    width: 1200px;
    height: 798px;
    overflow: hidden;
    background: var(--label-white);
  }
  .label {
    position: relative;
    width: 1200px;
    height: 798px;
    background: var(--label-red);
    overflow: hidden;
  }
  .label__panel {
    position: absolute;
    left: 10px;
    right: 10px;
    top: 266px;
    bottom: 10px;
    background: var(--label-white);
  }
  .brand-name {
    position: absolute;
    left: 0;
    right: 0;
    top: 84px;
    text-align: center;
    font-family: "Oswald", sans-serif;
    font-weight: 600;
    font-size: 82px;
    line-height: 1;
    letter-spacing: 1px;
    text-transform: uppercase;
    color: var(--label-white);
  }
  .fresh-flag {
    position: absolute;
    left: 18px;
    top: 304px;
    width: 265px;
    height: 186px;
  }
  .fresh-flag__word {
    position: absolute;
    left: 40px;
    top: 362px;
    font-family: "Anton", sans-serif;
    font-size: 86px;
    line-height: 1;
    color: var(--ink-black);
    transform: rotate(-11deg);
    transform-origin: left top;
    letter-spacing: 1px;
  }
  .product-info {
    position: absolute;
    left: 61px;
    top: 653px;
    color: var(--ink-black);
    font-family: "Encode Sans Condensed", sans-serif;
  }
  .product-info__origin {
    font-family: "Oswald", sans-serif;
    font-weight: 600;
    font-size: 28px;
    line-height: 32px;
    letter-spacing: -0.3px;
  }
  .product-info__storage {
    font-weight: 400;
    font-size: 29px;
    line-height: 32px;
    letter-spacing: -0.5px;
  }
  .website {
    position: absolute;
    right: 51px;
    top: 736px;
    font-family: "Encode Sans Condensed", sans-serif;
    font-weight: 700;
    font-size: 29px;
    line-height: 1;
    color: var(--ink-black);
  }
</style>
</head>
<body>
  <main class="label">
    <div class="label__panel"></div>

    <h1 class="brand-name">Lantern and Hill</h1>

    <svg class="fresh-flag" viewBox="0 0 265 186" aria-hidden="true">
      <path d="M19 118 Q16 78 40 70 Q90 62 130 42 Q170 22 259 12 L260 232 Z" fill="none"/>
      <path class="fresh-flag__shadow" d="M36 180 L260 126 L260 16 L238 18 L240 120 Q150 130 120 142 Q80 160 36 170 Z" fill="var(--ink-black)"/>
      <path class="fresh-flag__shape" d="M6 70 Q8 50 30 46 Q90 40 130 26 Q175 10 250 8 L251 120 Q190 124 140 142 Q90 160 26 176 Q8 176 6 150 Z" fill="var(--fresh-yellow)"/>
    </svg>
    <div class="fresh-flag__word">FRESH</div>

    <div class="product-info">
      <p class="product-info__origin">PRODUCT OF USA</p>
      <p class="product-info__storage">Keep Refrigerated</p>
    </div>

    <p class="website">www.lantern-hill.com</p>
  </main>
</body>
</html>
```